Webdesign für ambulanten Intensivpflegedienst
Zielgruppe
Moin liebe Designer,
vorab einen guten Start ins neue Jahr :) Wir sind ein ambulanter Intensivpflegedienst im Speckgürtel Hamburgs. Wir betreuen seit über 20 Jahren Kinder, Jugendliche und Erwachsene, die eine dauerhafte Überwachung und Betreuung benötigen. Dabei sind unsere Pflegefachkräfte dauerhaft vor Ort. Wir haben kaum Fluktuation, eine hohe Mitarbeiterzufriedenheit und erhalten auch weiterhin Bewerbungen in diesem hart umkämpften Markt, leider ist es uns noch nicht gelungen diese positiven Aspekte öffentlichkeitswirksam nach außen zu tragen.
Aufgabenstellung
Neues Corporate Identity Design für eine Wordpress oder Joomla Seite.
Bilder können gerne aus bildmarktplatz-ost.com oder ähnlichen Marktplätzen vorgeschlagen werden. Dabei bitten wir auf Bilder mit älteren Menschen im Rollstuhl oder Pflegekräfte in Dienstkleidung zu verzichten, da unsere Mitarbeitenden unseren Kund:innen nicht das Bild einer Intensivstation vermitteln wollen, sondern ein würdiges Leben daheim oder unterwegs. Ebenso nutzen unsere Kund:innen Elektro-Rollstühle, sind mobil, gehen zur Schule oder in die Uni.
Gerne kann auch die Geschichte oder Bilder eines Betroffenen benutzt werden. Einige unserer Kund:innen spielen E-Rolli-Fußball: https://www.sportverband-muster.de/nachhaltigkeitsmanagement/news/news-detail/?tx_news_pi1%5Bnews%5D=648213 oder engagieren sich für benachteiligte.
Ein Gesichtsbuchs oder Bildfluss Account besteht nicht. Ein Nerv und KarriereNetz Profil sind im Aufbau.
Wir haben uns ein paar Websites angesehen, die auch unseren Wünschen entsprechen, diese können wir gerne auf Anfrage verschicken. Als Referenz unsere alte Website: https://seitenspeicher-beispiel.org/web/20190107114418/https://taleb-pflegedienst.de/ oder unsere aktuellen Stellenanzeigen: https://www.inseratbrett-muster.de/s-bestandsliste.html?userId=71564820
Als Thema/Farbkonzept für unsere Website würden wir gerne die Nähe zur Lüneburger Heide nutzen und auch in diesem Stil/ Farben etc. die Website gestalten. Beispielhaft kann dafür die Tourismusseite der Lüneburger Heide genommen werden: https://www.gruenland-ferien-beispiel.de/natur
Ersichtlich sind unsere Stellenanzeigen in blau gehalten und eher dem Wasser zugeneigt, wie auch unser Logo aus einem Fisch besteht und unsere alte Website eher an den ländlichen Raum. Da wir Kunden sowohl in Hamburg als auch in Schleswig-Holstein und zuletzt überwiegend in Niedersachsen (Lüneburger Heide) betreuen, würden wir uns freuen, wenn die Nähe zum Wasser und der Heide vereint werden kann.
Wir haben hier be..

```html
<!DOCTYPE html>
<html lang="de">
<head>
<meta charset="utf-8">
<title>Taleb Pflegedienst – Webdesign</title>
<link href="https://fonts.googleapis.com/css2?family=Arimo:wght@400;700&display=swap" rel="stylesheet">
<style>
:root{
  --blue:#3bb4ea;
  --blue-dark:#1c7fb4;
  --blue-pale:#e8f5fc;
  --green:#6fb43f;
  --green-light:#b9e48d;
  --purple:#a8449c;
  --purple-light:#eaa5df;
  --ink:#1d1d1f;
  --muted:#6d6d72;
  --paper:#ffffff;
  --stage:#eef1f4;
}
*{margin:0;padding:0;box-sizing:border-box}
html,body{width:1036px;height:1200px;overflow:hidden}
body{background:var(--stage);font-family:"Arimo",Arial,sans-serif;color:var(--ink);position:relative}
.page{position:absolute;top:20px;width:490px;background:var(--paper);box-shadow:0 4px 18px rgba(0,0,0,.18);overflow:hidden}
.page-home{left:18px}
.page-services{left:528px}
section{position:relative;overflow:hidden}

/* navigation */
.nav{height:30px;display:flex;align-items:center;padding:0 26px;font-size:6.5px;font-weight:700;position:relative;background:#fff}
.nav a{color:var(--ink);text-decoration:none;margin-right:16px}
.nav .brand{margin:0 22px 0 8px;font-size:10px;font-weight:700;white-space:nowrap}
.nav .contact{position:absolute;right:0;top:0;height:30px;width:82px;background:var(--blue);clip-path:polygon(24% 0,100% 0,100% 100%,0 100%);color:#fff;display:flex;align-items:center;justify-content:flex-end;padding-right:20px;margin:0}

/* hero */
.hero{height:140px;color:#fff}
.hero-water{position:absolute;inset:0;background:linear-gradient(180deg,#8fd0ee 0%,#45a9d8 45%,#1b78ad 100%)}
.hero-photo{position:absolute;inset:0;clip-path:polygon(78% 0,100% 0,100% 100%,50% 100%)}
.photo-heath{background:linear-gradient(170deg,#3f6d25 0%,#6d9a3d 40%,#a9b27a 65%,#b98ec7 82%,#8a7f6a 100%)}
.photo-people{background:linear-gradient(160deg,#d8b08a 0%,#f0e2d2 45%,#9c8b7a 100%)}
.hero-stripe{position:absolute;inset:0;background:var(--blue);clip-path:polygon(75% 0,78% 0,50% 100%,47% 100%)}
.hero h1{position:absolute;left:30px;top:32px;font-size:15.5px;font-weight:700;letter-spacing:.2px}
.hero .hero-sub{position:absolute;left:30px;top:58px;font-size:15px;line-height:1.15}

/* shared type */
.eyebrow{font-size:4.5px;color:var(--blue);text-transform:uppercase;letter-spacing:.3px}
.eyebrow.green{color:var(--green)}
h2{font-size:13px;font-weight:700;margin:2px 0 5px}
.rule{width:20px;height:1px;background:var(--blue);margin-bottom:6px}
.rule.light{background:rgba(255,255,255,.8);margin:0 auto 6px}
.copy{font-size:4.6px;line-height:1.55;color:var(--muted)}
.btn{display:inline-block;background:var(--blue);color:#fff;font-size:5px;font-weight:700;padding:3px 12px;border-radius:8px;box-shadow:0 2px 3px rgba(0,0,0,.2);margin-top:8px}
.center{text-align:center}
.photo{position:absolute;border:3px solid #fff;box-shadow:0 2px 5px rgba(0,0,0,.3)}

/* colour bands */
.band-green{background:linear-gradient(90deg,var(--green-light),var(--green));color:#fff;text-align:center;padding:12px 30px 0}
.band-green h2{font-size:11.5px}
.band-green .copy,.band-purple .copy,.band-blue .copy{color:rgba(255,255,255,.9)}
.band-purple{background:linear-gradient(135deg,var(--purple-light),var(--purple));color:#fff;text-align:center;padding:16px 30px 0}
.band-blue{background:linear-gradient(180deg,#46b2e2,#1f86bd);color:#fff;text-align:center;padding:18px 20px 0}

.cards{display:flex;gap:8px;justify-content:center;margin-top:10px}
.card{background:#fff;border-radius:5px;width:116px;padding:8px 8px 7px;text-align:center;color:var(--ink);box-shadow:0 2px 5px rgba(0,0,0,.2)}
.card h3{font-size:6.3px;font-weight:700;margin-bottom:4px;line-height:1.2}
.card .copy{color:var(--muted)!important}
.card svg{width:14px;height:14px;display:block;margin:0 auto 3px}

/* split section */
.split{display:flex;align-items:center;padding:0 30px;gap:20px}
.split .media{position:relative;width:180px;height:100%}
.split .text{flex:1}

/* services diagonal */
.services{height:140px;background:var(--blue-pale)}
.services .panel{position:absolute;inset:0;background:var(--blue);clip-path:polygon(65% 0,100% 0,100% 100%,40% 100%)}
.services .left{position:absolute;left:30px;top:20px;width:180px}
.services .right{position:absolute;left:318px;top:38px;width:120px;color:#fff;border-left:1px solid rgba(255,255,255,.7);padding-left:8px}
.services h4{font-size:7.5px;margin-bottom:4px}
.services ul{list-style:none;font-size:4.3px;line-height:1.9}
.services li::before{content:"•";margin-right:3px}

/* carousel */
.carousel{height:80px;display:flex;gap:4px;position:relative}
.slide{flex:1}
.slide.mid{background:#3d4348;color:#fff;text-align:center;display:flex;flex-direction:column;justify-content:center;padding:0 16px}
.slide.mid h5{font-size:6px;font-weight:700;margin-bottom:4px;line-height:1.2}
.slide.mid .copy{color:rgba(255,255,255,.85)}
.arrow{position:absolute;top:34px;width:0;height:0;border-top:5px solid transparent;border-bottom:5px solid transparent}
.arrow.prev{left:18px;border-right:7px solid #fff}
.arrow.next{right:18px;border-left:7px solid #fff}

/* contact */
.contact-block{height:120px}
.contact-bg{position:absolute;inset:0;background:linear-gradient(180deg,#2f3a2a,#5d6a4a 60%,#6d7a52)}
.contact-card{position:absolute;left:113px;top:14px;width:264px;height:92px;background:#fff;border-radius:5px;text-align:center;padding:6px 18px}
.contact-card h2{font-size:10px;margin:2px 0 3px}
.contact-cols{display:flex;justify-content:center;gap:26px;margin-top:6px;font-size:4.3px;line-height:1.5;text-align:left}
.contact-cols .blue{color:var(--blue)}

/* footer */
.footer{height:50px;background:linear-gradient(90deg,#4ab9ea,#2a8fc6);color:#fff;display:flex;align-items:center;justify-content:space-between;padding:0 40px;font-size:4.5px;line-height:1.6}
.footer .brand{font-size:11px;font-weight:700}
.footbar{height:10px;background:#2b2f33}
</style>
</head>
<body>

<!-- Startseite -->
<div class="page page-home">
  <nav class="nav">
    <a>Über Taleb</a><a>Leistungen</a><a>Leitbild</a>
    <span class="brand">Taleb Pflegedienst</span>
    <a>Geschichten</a><a>Jobs</a>
    <a class="contact">Kontakt</a>
  </nav>

  <section class="hero">
    <div class="hero-water" role="img" aria-label="Ruhige blaue Wasserfläche"></div>
    <div class="hero-photo photo-heath" role="img" aria-label="Heidelandschaft mit Weg, Bäumen und Bank"></div>
    <div class="hero-stripe"></div>
    <h1>IN SEINER EINZIGARTIGKEIT</h1>
    <p class="hero-sub">STEHT DER MENSCH<br>IM MITTELPUNKT</p>
  </section>

  <section class="band-green" style="height:110px">
    <h2>Ihr ambulanter Intensivpflegedienst</h2>
    <div class="rule light"></div>
    <p class="copy">Wir begleiten Menschen jeden Alters zu Hause, in der Schule, an der Uni<br>und unterwegs – mit festen Teams und viel Zeit für jeden Tag.</p>
    <div class="cards">
      <div class="card"><h3>KINDER</h3><p class="copy">Vertraute Pflege, die den Alltag in Familie, Kita und Schule möglich macht.</p></div>
      <div class="card"><h3>JUGENDLICHE</h3><p class="copy">Unterstützung auf dem Weg in Ausbildung, Freizeit und mehr Selbstständigkeit.</p></div>
      <div class="card"><h3>ERWACHSENE</h3><p class="copy">Dauerhafte Betreuung für ein würdiges Leben daheim und unterwegs.</p></div>
    </div>
  </section>

  <section class="split" style="height:130px">
    <div class="media">
      <div class="photo photo-heath" style="left:0;top:16px;width:66px;height:46px" role="img" aria-label="Heide im Abendlicht"></div>
      <div class="photo" style="left:16px;top:44px;width:82px;height:62px;background:linear-gradient(160deg,#6f8da3,#c9a98c 55%,#5a4a45)" role="img" aria-label="Gruppe lächelnder Mitarbeitender"></div>
    </div>
    <div class="text">
      <p class="eyebrow">Über uns</p>
      <h2>Wir von Taleb</h2>
      <div class="rule"></div>
      <p class="copy">Seit über zwanzig Jahren pflegen wir Menschen, die dauerhaft Begleitung brauchen. Unser Team bleibt, kennt die Familien und nimmt sich Zeit. So entsteht Vertrauen, das man im Alltag spürt und auf das man bauen kann.</p>
      <span class="btn">Mehr erfahren</span>
    </div>
  </section>

  <section class="services">
    <div class="panel"></div>
    <div class="left">
      <p class="eyebrow">Pflegeleistungen</p>
      <h2>Von Mensch zu Mensch</h2>
      <p class="copy">Unsere Fachkräfte sind rund um die Uhr vor Ort. Sie überwachen, versorgen und begleiten, ohne den Alltag zu bestimmen.</p>
      <p class="copy" style="margin-top:4px">Ob Schulweg, Ausflug oder ein ruhiger Abend zu Hause – wir richten uns nach den Menschen, die wir betreuen, und ihren Wünschen.</p>
      <span class="btn">Mehr erfahren</span>
    </div>
    <div class="right">
      <h4>Leistungen</h4>
      <ul><li>Intensivpflege rund um die Uhr</li><li>Beatmung und Überwachung</li><li>Begleitung in Schule und Uni</li><li>Assistenz bei Ausflügen</li><li>Beratung für Angehörige</li><li>Feste Bezugspflege im Team</li></ul>
    </div>
  </section>

  <section class="band-purple" style="height:140px">
    <p class="eyebrow" style="color:#fff">Leitbild &amp; Werte</p>
    <h2>Seit 20 Jahren persönlich da</h2>
    <div class="rule light"></div>
    <p class="copy">Unsere Werte leiten jeden Einsatz – im Team, bei den Familien<br>und überall dort, wo wir gebraucht werden.</p>
    <div class="cards">
      <div class="card"><svg viewBox="0 0 14 14" fill="none" stroke="#d98ccf"><circle cx="7" cy="5" r="3"/><path d="M3 13h8M5 10h4"/></svg><h3>STÄNDIGE<br>WEITERBILDUNG</h3><p class="copy">Regelmäßige Schulungen halten unser Wissen aktuell.</p></div>
      <div class="card"><svg viewBox="0 0 14 14" fill="none" stroke="#d98ccf"><circle cx="4" cy="5" r="2"/><circle cx="10" cy="5" r="2"/><path d="M1 12c0-3 6-3 6 0M7 12c0-3 6-3 6 0"/></svg><h3>GUTE<br>KOMMUNIKATION</h3><p class="copy">Offener Austausch mit Familien und Ärzten.</p></div>
      <div class="card"><svg viewBox="0 0 14 14" fill="none" stroke="#d98ccf"><path d="M7 12L2 7a3 3 0 015-4 3 3 0 015 4z"/></svg><h3>WÜRDE, RESPEKT<br>&amp; VERTRAUEN</h3><p class="copy">Jeder Mensch wird so begleitet, wie er es möchte.</p></div>
    </div>
    <span class="btn">Mehr erfahren</span>
  </section>

  <section style="height:50px;background:#f1f8ea;padding:10px 30px 0">
    <p class="eyebrow">Ganz nah am Menschen</p>
    <h2 style="margin-bottom:2px">Besondere Geschichten</h2>
    <p class="copy" style="width:300px">Menschen, die wir begleiten, erzählen von Sport, Reisen und ihrem Alltag.</p>
    <span class="btn" style="position:absolute;right:30px;top:28px;margin:0">Mehr erfahren</span>
  </section>
  <section class="carousel">
    <div class="slide" style="background:linear-gradient(160deg,#6b5a4c,#c9a282 55%,#3b342f)" role="img" aria-label="Lachender Junge"></div>
    <div class="slide mid" role="img" aria-label="Rollstuhlfußball-Mannschaft in der Halle"><h5>E-ROLLI-FUSSBALL IN<br>BARMSTEDT</h5><p class="copy">Training jede Woche, Turniere im ganzen Land und viel Teamgeist.</p></div>
    <div class="slide" style="background:linear-gradient(160deg,#8a9aa6,#e4d6c6 55%,#6d6258)" role="img" aria-label="Junge Frau im Rollstuhl am Arbeitsplatz"></div>
    <span class="arrow prev"></span><span class="arrow next"></span>
  </section>

  <section class="split" style="height:140px">
    <div class="text">
      <p class="eyebrow">Jobs</p>
      <h2 style="line-height:1.05">Bewerben Sie<br>sich bei uns!</h2>
      <div class="rule"></div>
      <p class="copy">Wir suchen Pflegefachkräfte, die Menschen mit Herz begleiten. Bei uns erwarten Sie feste Teams, faire Dienstpläne und echte Wertschätzung im Alltag.</p>
      <span class="btn">Mehr erfahren</span>
    </div>
    <div class="media">
      <div class="photo" style="left:40px;top:14px;width:62px;height:56px;background:linear-gradient(180deg,#b9cde0,#d6b58e 55%,#2e4f6a)" role="img" aria-label="Hafen einer Stadt am Wasser"></div>
      <div class="photo" style="left:70px;top:38px;width:64px;height:84px;background:linear-gradient(170deg,#e8e4de,#d7b494 45%,#f3efe8)" role="img" aria-label="Frau beim Telefonieren"></div>
    </div>
  </section>

  <section class="contact-block">
    <div class="contact-bg" role="img" aria-label="Bank am Wasser in der Heide"></div>
    <div class="contact-card">
      <svg width="18" height="11" viewBox="0 0 18 11" fill="none" stroke="#3bb4ea"><rect x=".5" y=".5" width="17" height="10"/><path d="M.5 .5l8.5 6 8.5-6"/></svg>
      <h2>Nehmen Sie Kontakt auf</h2>
      <p class="copy">Rufen Sie uns an oder schreiben Sie uns. Wir melden uns schnell<br>und beraten Sie gern persönlich und ohne Verpflichtung.</p>
      <div class="contact-cols">
        <div><b>Taleb Pflegedienst</b><br>Heidweg 14<br>21220 Musterdorf</div>
        <div class="blue">Tel. 040 / 12 3456 789<br>info@taleb-pflegedienst.de</div>
      </div>
    </div>
  </section>

  <footer class="footer">
    <span class="brand">Taleb Pflegedienst</span>
    <span class="center">Impressum<br>AGB<br>Datenschutz</span>
    <span class="center"><b>Taleb Pflegedienst</b><br>Heidweg 14<br>21220 Musterdorf</span>
  </footer>
  <div class="footbar"></div>
</div>

<!-- Leistungsseite -->
<div class="page page-services">
  <nav class="nav">
    <a>Über Taleb</a><a>Leistungen</a><a>Leitbild</a>
    <span class="brand">Taleb Pflegedienst</span>
    <a>Geschichten</a><a>Jobs</a>
    <a class="contact">Kontakt</a>
  </nav>

  <section class="hero">
    <div class="hero-water" role="img" aria-label="Ruhige blaue Wasserfläche"></div>
    <div class="hero-photo photo-people" role="img" aria-label="Ältere Dame und junge Begleiterin lachen gemeinsam"></div>
    <div class="hero-stripe"></div>
    <h1>UNSERE LEISTUNGEN</h1>
    <p class="hero-sub">FÜR SEHR BESONDERE<br>MENSCHEN</p>
  </section>

  <section class="band-green" style="height:70px">
    <h2>Nähe aus Leidenschaft</h2>
    <div class="rule light"></div>
    <p class="copy">Wir pflegen dort, wo Menschen leben: zu Hause, in der Schule und unterwegs.<br>Feste Teams sorgen für Sicherheit, Ruhe und ein vertrautes Miteinander.<br>So bleibt Raum für Freunde, Hobbys und einen selbstbestimmten Alltag.</p>
  </section>

  <section class="split" style="height:170px">
    <div class="media">
      <div class="photo" style="left:0;top:24px;width:64px;height:72px;background:linear-gradient(160deg,#c9a07a,#e9dccb 50%,#8b7358)" role="img" aria-label="Zwei Frauen kochen zusammen"></div>
      <div class="photo" style="left:34px;top:70px;width:64px;height:66px;background:linear-gradient(160deg,#7a8fb8,#e2c9b2 55%,#c35a4a)" role="img" aria-label="Lachendes Mädchen vor einem Bücherregal"></div>
    </div>
    <div class="text">
      <p class="eyebrow green">Ganz nah an unseren Kunden</p>
      <h2>Echtes Interesse</h2>
      <div class="rule"></div>
      <p class="copy">Wir hören zu, bevor wir planen. Jede Betreuung beginnt mit einem Gespräch über Wünsche, Gewohnheiten und Ziele. Daraus entsteht ein Alltag, der zu den Menschen passt.</p>
      <p class="copy" style="margin-top:5px">Unsere Fachkräfte bleiben lange im selben Haushalt. Das schafft Nähe und Verlässlichkeit für Familien und gibt allen Beteiligten Sicherheit.</p>
    </div>
  </section>

  <section class="band-blue" style="height:300px">
    <p class="eyebrow" style="color:#fff">Für uns selbstverständlich</p>
    <h2>Unser Pflegeservice</h2>
    <div class="rule light"></div>
    <p class="copy">Qualität, Offenheit und Respekt prägen jeden unserer Einsätze.</p>
    <div class="cards">
      <div class="card"><svg viewBox="0 0 14 14" fill="none" stroke="#555"><circle cx="7" cy="5" r="3"/><path d="M3 13h8M5 10h4"/></svg><h3>STÄNDIGE<br>WEITERBILDUNG</h3><p class="copy">Regelmäßige Schulungen für das ganze Team.</p></div>
      <div class="card"><svg viewBox="0 0 14 14" fill="none" stroke="#555"><circle cx="4" cy="5" r="2"/><circle cx="10" cy="5" r="2"/><path d="M1 12c0-3 6-3 6 0M7 12c0-3 6-3 6 0"/></svg><h3>GUTE<br>KOMMUNIKATION</h3><p class="copy">Klare Absprachen mit Familien und Ärzten.</p></div>
      <div class="card"><svg viewBox="0 0 14 14" fill="none" stroke="#555"><path d="M7 12L2 7a3 3 0 015-4 3 3 0 015 4z"/></svg><h3>WÜRDE, RESPEKT<br>&amp; VERTRAUEN</h3><p class="copy">Begleitung ganz nach eigenem Wunsch.</p></div>
    </div>
    <div class="cards">
      <div class="card"><svg viewBox="0 0 14 14" fill="none" stroke="#555"><circle cx="7" cy="5" r="3"/><path d="M3 13h8M5 10h4"/></svg><h3>STÄNDIGE<br>WEITERBILDUNG</h3><p class="copy">Fachwissen, das immer aktuell bleibt.</p></div>
      <div class="card"><svg viewBox="0 0 14 14" fill="none" stroke="#555"><circle cx="4" cy="5" r="2"/><circle cx="10" cy="5" r="2"/><path d="M1 12c0-3 6-3 6 0M7 12c0-3 6-3 6 0"/></svg><h3>GUTE<br>KOMMUNIKATION</h3><p class="copy">Kurze Wege und feste Ansprechpartner.</p></div>
      <div class="card"><svg viewBox="0 0 14 14" fill="none" stroke="#555"><path d="M7 12L2 7a3 3 0 015-4 3 3 0 015 4z"/></svg><h3>WÜRDE, RESPEKT<br>&amp; VERTRAUEN</h3><p class="copy">Achtsam im Umgang, jeden Tag.</p></div>
    </div>
    <div class="cards">
      <div class="card"><svg viewBox="0 0 14 14" fill="none" stroke="#555"><circle cx="7" cy="5" r="3"/><path d="M3 13h8M5 10h4"/></svg><h3>STÄNDIGE<br>WEITERBILDUNG</h3><p class="copy">Neue Methoden sicher im Alltag.</p></div>
      <div class="card"><svg viewBox="0 0 14 14" fill="none" stroke="#555"><circle cx="4" cy="5" r="2"/><circle cx="10" cy="5" r="2"/><path d="M1 12c0-3 6-3 6 0M7 12c0-3 6-3 6 0"/></svg><h3>GUTE<br>KOMMUNIKATION</h3><p class="copy">Zuhören, erklären und gemeinsam planen.</p></div>
      <div class="card"><svg viewBox="0 0 14 14" fill="none" stroke="#555"><path d="M7 12L2 7a3 3 0 015-4 3 3 0 015 4z"/></svg><h3>WÜRDE, RESPEKT<br>&amp; VERTRAUEN</h3><p class="copy">Verlässlich an der Seite der Familien.</p></div>
    </div>
  </section>

  <section style="height:80px;padding:18px 30px 0;text-align:center">
    <p class="eyebrow green">Ganz nah am Menschen</p>
    <h2>Besondere Angebote</h2>
    <p class="copy">Gemeinsam unterwegs: Ausflüge, Urlaube und Freizeit mit vertrauter<br>Begleitung. Wir planen mit und sorgen dafür, dass jede Reise gelingt.</p>
  </section>
  <section class="carousel">
    <div class="slide" style="background:linear-gradient(160deg,#5b6068,#a7a39c 55%,#3a3d42)" role="img" aria-label="Rollstuhl an einem Fahrzeug mit Rampe"></div>
    <div class="slide mid" role="img" aria-label="Heller Raum in einer Ferienunterkunft"><h5>ERHOLSAMEN URLAUB<br>BAD BEVENSEN</h5><p class="copy">Ruhige Tage in der Heide mit Pflege rund um die Uhr.</p></div>
    <div class="slide" style="background:linear-gradient(160deg,#c6d1d8,#d8b9a0 55%,#44505c)" role="img" aria-label="Junge Frau und älterer Mann im Gespräch"></div>
    <span class="arrow prev"></span><span class="arrow next"></span>
  </section>

  <section class="services" style="height:150px;margin-top:40px">
    <div class="panel" style="clip-path:polygon(60% 0,100% 0,100% 100%,35% 100%)"></div>
    <div class="left" style="top:30px">
      <p class="eyebrow">Pflegeleistungen</p>
      <h2>Lorem Ipsum</h2>
      <p class="copy">Wir erstellen mit jeder Familie einen eigenen Pflegeplan und passen ihn an, wenn sich das Leben verändert.</p>
      <p class="copy" style="margin-top:4px">Kurze Wege, feste Teams und klare Absprachen machen den Alltag leichter.</p>
    </div>
    <div class="right" style="left:310px;top:30px">
      <h4>Aufzählung</h4>
      <ul><li>Beatmungspflege zu Hause</li><li>Begleitung zur Schule</li><li>Unterstützung im Studium</li><li>Assistenz bei Freizeit und Sport</li><li>Pflege auf Reisen</li><li>Beratung für Angehörige</li></ul>
    </div>
  </section>
  <div class="footbar"></div>
</div>

</body>
</html>
```